1 Home page redesign for existing repair service site.

We need a refresh of our existing website that looks more 2017. We have made a mockup of the content that we want and a sample of where we want it. Nothing is set in stone, if you have better ideas of where things should go, feel free.

You can see our current site at http://www.tokelmo.gr

The colors should stay orange/black/grey.

In many of the "boxes/banners" we will need images. Feel free to find in glade barn as we have an account.

We have made notes throughout the wireframe that we have attached on what we are looking for. Let us know if you have any questions. Thanks.

Target Market(s)

People using technology and breaking it

Industry/Entity Type

It Service

Number of Pages Required

1 page

Font styles to use
Sans Serif

Requirements
Must have
• Must have a modern, professional look and feel. Need custom graphics and icons.

```html
<!DOCTYPE html>
<html lang="en">
<head>
<meta charset="utf-8">
<title>Tokelmo – Home</title>
<link href="https://fonts.googleapis.com/css2?family=Dosis:wght@300;400;500;600&family=Titillium+Web:wght@400;600&display=swap" rel="stylesheet">
<style>
:root{
  --orange:#f7993f;
  --orange-deep:#f36f21;
  --ink:#4a4a4a;
  --muted:#8d8d8d;
  --light:#f5f5f5;
  --band:#5a5a5a;
  --footer:#232323;
  --footer-base:#141414;
  --blue:#29a9e0;
  --white:#ffffff;
}
*{box-sizing:border-box;margin:0;padding:0}
html,body{width:1200px;height:880px;overflow:hidden}
body{position:relative;font-family:"Dosis",sans-serif;background:var(--white);color:var(--ink)}
.abs{position:absolute}

.hero{left:0;top:0;width:1200px;height:142px;background:radial-gradient(ellipse at 45% 90%,#6a3524 0%,#2a1612 40%,#0c0909 80%)}
.feature-card{top:0;width:176px;height:101px;background:rgba(30,30,30,.78);border-radius:0 0 3px 3px;padding:0 14px 0 18px;color:#e8e8e8;font-family:"Dosis",sans-serif;font-size:10px;line-height:12px}

.options{left:0;top:142px;width:1200px;height:48px;background:var(--orange);color:var(--white)}
.options-title{left:153px;top:8px;font-family:"Titillium Web",sans-serif;font-size:17px;line-height:16px;padding-right:25px;border-right:1px solid rgba(255,255,255,.5);height:34px}
.options-title b{font-weight:600;display:block}
.option{top:0;height:48px;display:flex;align-items:center;gap:14px;font-family:"Titillium Web",sans-serif;font-size:13.5px;letter-spacing:.4px}

.testimonials{left:0;top:190px;width:1200px;height:320px;background:var(--light)}
.section-title{left:0;top:20px;width:1200px;text-align:center;font-family:"Dosis",sans-serif;font-weight:500;font-size:30px;color:#333}
.section-title span{color:var(--orange-deep)}
.quote-card{top:76px;width:304px;height:200px;background:var(--white);border-top:5px solid var(--orange-deep);border-radius:3px}
.quote-mark{font-family:Georgia,serif;font-size:80px;color:#ececec;line-height:1;font-weight:bold}
.quote-text{left:24px;top:31px;width:256px;text-align:center;font-size:9px;line-height:19.2px;color:var(--muted);font-weight:300}
.quote-author{left:0;top:163px;width:304px;text-align:center;font-size:10px;color:#444}
.quote-author span{color:var(--orange-deep)}
.nav-arrow{top:163px}

.cta{left:0;top:556px;width:1200px;height:44px;background:var(--band)}
.cta-text{left:344px;top:11px;color:var(--white);font-family:"Titillium Web",sans-serif;font-size:15.5px}
.cta-button{left:696px;top:8px;width:128px;height:26px;background:var(--blue);color:var(--white);font-size:7.5px;font-weight:600;text-align:center;line-height:25px;border-radius:2px;border-bottom:2px solid #1d7fa8;letter-spacing:.2px}

.footer{left:0;top:600px;width:1200px;height:256px;background:var(--footer);color:var(--white)}
.footer-heading{top:50px;font-family:"Titillium Web",sans-serif;font-weight:600;font-size:13.5px;border-bottom:1px solid #aaa;line-height:17px}
.quick-links{left:115px;top:88px;list-style:none;font-family:"Titillium Web",sans-serif;font-size:9.6px;line-height:19.2px;font-weight:600}
.quick-links .active{color:var(--blue)}
.social-dot{width:18px;height:18px;border:1.4px solid var(--white)}
.blog-date{left:440px;width:22px;text-align:center;color:var(--blue);font-size:7.4px;font-weight:600;line-height:8.5px}
.blog-title{left:495px;width:200px;font-size:8.6px;line-height:9px;color:#eee}
.blog-rule{left:495px;width:200px;height:1px;background:#666}
.newsletter-text{left:755px;top:90px;font-family:"Titillium Web",sans-serif;font-size:9.6px;letter-spacing:.2px}
.newsletter-input{left:756px;top:107px;width:320px;height:16px;border:1px solid #999;background:#3a3a3a;border-radius:2px;color:#bbb;font-size:8px;padding-left:8px;line-height:14px}
.newsletter-submit{left:756px;top:131px;width:160px;height:16px;background:var(--blue);border-radius:2px;font-size:9px;font-weight:600;text-align:center;line-height:16px}
.copyright{left:0;top:856px;width:1200px;height:24px;background:var(--footer-base);color:#ddd;font-family:"Titillium Web",sans-serif;font-size:7.6px;text-align:center;line-height:24px}
</style>
</head>
<body>

<section class="hero abs" role="img" aria-label="Blurred photo of a technician's workbench in dark warm tones">
  <div class="feature-card abs" style="left:218px">passwords and more. We don't believe your device needs to go behind a closed door to to be repaired. All Tokelmo locations are designed to have the technicians in open view so you can keep an eye on your device.</div>
  <div class="feature-card abs" style="left:414px">procedure before and after the repair gives our customers the highest quality repair available.</div>
  <div class="feature-card abs" style="left:610px">trained and tested in all device repairs. They are continuously being trained in new repairs and repair processes that are up to the highest Tokelmo standards.</div>
  <div class="feature-card abs" style="left:806px">technicians that we give our customers a lifetime guarantee on almost all our repairs.</div>
</section>

<nav class="options abs" aria-label="Repair options">
  <div class="options-title abs"><b>Repair</b>Options</div>
  <div class="option abs" style="left:330px">
    <svg width="58" height="26" viewBox="0 0 58 26" fill="#fff"><path d="M4 18c0-5 6-7 12-8 4-6 10-8 18-8 7 0 11 3 15 8 5 1 8 3 8 8v2H4z"/><circle cx="16" cy="21" r="5" fill="#fff" stroke="#f7993f" stroke-width="2"/><circle cx="45" cy="21" r="5" fill="#fff" stroke="#f7993f" stroke-width="2"/><path d="M20 10c3-4 7-5 12-5v5zM35 5c5 0 8 2 10 5H35z" fill="#f7993f"/></svg>
    <span>Find a store near you</span>
  </div>
  <div class="option abs" style="left:622px">
    <svg width="34" height="34" viewBox="0 0 34 34" fill="#fff"><path d="M17 2l14 7-14 7-14-7z"/><path d="M3 11l13 7v14L3 25z"/><path d="M31 11l-13 7v14l13-7z"/><path d="M8 8l14 7v5l-3 1v-5L5 9z" fill="#f7993f"/></svg>
    <span>Send us your device</span>
  </div>
  <div class="option abs" style="left:884px">
    <svg width="32" height="34" viewBox="0 0 32 34" fill="#fff"><rect x="13" y="2" width="16" height="16" rx="1"/><rect x="1" y="20" width="5" height="12"/><path d="M7 21h8c3 0 4 2 7 2h8v5l-12 4H7z"/></svg>
    <span>Free pickup in Athens</span>
  </div>
</nav>

<section class="testimonials abs">
  <h2 class="section-title abs">Client <span>Testimonials</span></h2>

  <svg class="nav-arrow abs" style="left:120px" width="12" height="22" viewBox="0 0 12 22"><path d="M11 1L1 11l10 10" fill="none" stroke="#555" stroke-width="1.5"/></svg>
  <svg class="nav-arrow abs" style="left:1070px" width="12" height="22" viewBox="0 0 12 22"><path d="M1 1l10 10L1 21" fill="none" stroke="#555" stroke-width="1.5"/></svg>

  <article class="quote-card abs" style="left:138px">
    <span class="quote-mark abs" style="left:14px;top:8px">“</span>
    <span class="quote-mark abs" style="left:236px;top:68px">”</span>
    <p class="quote-text abs">For months my laptop was in meltdown mode. It was terribly slow and I was getting error messages and frequent shutdowns. Since my whole life is on it I was desperate for a better solution because I didn't want to say goodbye to my laptop or my files. Tokelmo saved all my precious files and now my computer is really fast! I recommend them without any hesitation. You guys are fantastic!</p>
    <p class="quote-author abs">Sofia L., <span>Chalandri</span></p>
  </article>

  <article class="quote-card abs" style="left:449px">
    <span class="quote-mark abs" style="left:14px;top:8px">“</span>
    <span class="quote-mark abs" style="left:236px;top:68px">”</span>
    <p class="quote-text abs">My phone 5 took a dive in the deep end of the pool and it never crossed my mind that it could be saved! Congratulations, you fixed it!</p>
    <p class="quote-author abs">Nikos D., <span>Thessaloniki</span></p>
  </article>

  <article class="quote-card abs" style="left:760px">
    <span class="quote-mark abs" style="left:14px;top:8px">“</span>
    <span class="quote-mark abs" style="left:236px;top:68px">”</span>
    <p class="quote-text abs">I just can't part with my phone ... I can't do anything without it! When my screen broke I went to Tokelmo feeling helpless. They replaced the screen incredibly fast in only 15 minutes!!! I was relieved, excited and grateful! Thank you is not enough!</p>
    <p class="quote-author abs">Eleni T., <span>Peristeri</span></p>
  </article>
</section>

<section class="cta abs">
  <p class="cta-text abs">Come and bring your broken product to us today!</p>
  <div class="cta-button abs">FIND A LOCATION NEAR YOU</div>
</section>

<footer class="footer abs">
  <h3 class="footer-heading abs" style="left:115px">Quick Links</h3>
  <h3 class="footer-heading abs" style="left:275px">Keep Connected</h3>
  <h3 class="footer-heading abs" style="left:440px">Blog</h3>
  <h3 class="footer-heading abs" style="left:755px">Newsletter</h3>

  <ul class="quick-links abs">
    <li>About Tokelmo</li>
    <li>Business Services</li>
    <li class="active">Schedule a Pickup</li>
    <li>Job openings</li>
    <li>Shipping Instructions</li>
    <li>Privacy policy</li>
    <li>Send your device with QuickDrop</li>
  </ul>

  <div class="social-dot abs" style="left:276px;top:92px;border-radius:50%"></div>
  <div class="social-dot abs" style="left:310px;top:92px;border-radius:50%"></div>
  <div class="social-dot abs" style="left:276px;top:119px;border-radius:50%"></div>
  <div class="social-dot abs" style="left:310px;top:119px;border-radius:4px"></div>
  <div class="social-dot abs" style="left:276px;top:145px;border-radius:50%"></div>
  <div class="social-dot abs" style="left:310px;top:145px;border-radius:4px"></div>
  <div class="social-dot abs" style="left:276px;top:172px;border-radius:50%"></div>

  <svg class="abs" style="left:440px;top:90px" width="20" height="12" viewBox="0 0 20 12"><path d="M1 11l9-9 9 9" fill="none" stroke="#aaa" stroke-width="1.2"/></svg>
  <div class="blog-date abs" style="top:116px">08/03<br>2017</div>
  <div class="blog-title abs" style="top:115px">81 year old woman learns programming from scratch and creates a phone app</div>
  <div class="blog-rule abs" style="top:141px"></div>
  <div class="blog-date abs" style="top:147px">20/02<br>2017</div>
  <div class="blog-title abs" style="top:150px">Tokelmo Corfu Seminar</div>
  <div class="blog-rule abs" style="top:171px"></div>
  <div class="blog-date abs" style="top:179px">17/02<br>2017</div>
  <div class="blog-title abs" style="top:181px">Orchard announces DevCon 2017</div>
  <svg class="abs" style="left:440px;top:209px" width="20" height="12" viewBox="0 0 20 12"><path d="M1 1l9 9 9-9" fill="none" stroke="#aaa" stroke-width="1.2"/></svg>

  <p class="newsletter-text abs">Subscribe to our newsletter to stay up to date with the latest news and offers</p>
  <div class="newsletter-input abs">Enter your email address</div>
  <div class="newsletter-submit abs">SUBMIT</div>
</footer>

<div class="copyright abs">Copyright © Tokelmo 2017</div>

</body>
</html>
```